CGSI application splash screen

We need a 1024x768 image for use as an application splash screen.
The image will be displayed full screen on an 10 inch industrial PC 1024x768 screen while our application is launching. The image should convey that the application is "Waiting for connection to Wi-Fi access point..." and include a graphic of the industrial PC connected to the access point via an Ethernet cable. A list of troubleshooting steps should be included at the bottom of the image. The troubleshooting steps should not be the main focus of the image and should be shown in a smaller font (but still readable at 1024x768 displayed on a 10 inch screen).
I will include a mock up of the general idea of what we are looking for as well as image files for the industrial PC, a screenshot of our application to show on the PC's screen and the AP.
For general look and feel and a sense of corporate branding please review our website https://copperlanegrowingsystems.com/. The splash screen should reflect corporate branding.
Users of our application
Agriculture

```html
<!DOCTYPE html>
<html lang="en">
<head>
<meta charset="utf-8">
<title>CGSI – Waiting for Wi-Fi access point</title>
<link href="https://fonts.googleapis.com/css2?family=Lexend:wght@400;500;600&display=swap" rel="stylesheet">
<style>
  :root {
    --brand-green: #45bd62;
    --white: #ffffff;
    --black: #000000;
    --device-dark: #2a2b2d;
    --device-mid: #4a4c50;
    --ap-light: #f1f2f2;
    --ap-shade: #d5d7d9;
  }
  html, body {
    margin: 0;
    padding: 0;
    overflow: hidden;
    background: var(--brand-green);
  }
  .splash {
    position: relative;
    width: 1200px;
    height: 900px;
    overflow: hidden;
    background: var(--brand-green);
    font-family: "Lexend", sans-serif;
    color: var(--white);
  }
  .brand {
    position: absolute;
    left: 38px;
    top: 40px;
    font-weight: 600;
    color: var(--white);
  }
  .brand-name {
    font-size: 62px;
    line-height: 1;
    letter-spacing: 2px;
  }
  .brand-full {
    margin-top: 10px;
    font-size: 17px;
    line-height: 1.1;
    width: 210px;
  }
  .headline {
    position: absolute;
    left: 200px;
    width: 800px;
    top: 36px;
    margin: 0;
    text-align: center;
    font-weight: 600;
    font-size: 74px;
    line-height: 79px;
    letter-spacing: 0.5px;
  }
  .diagram {
    position: absolute;
    left: 0;
    top: 0;
    width: 1200px;
    height: 620px;
  }
  .label {
    position: absolute;
    text-align: center;
    font-weight: 500;
    line-height: 1.08;
  }
  .label-computer {
    left: 40px;
    width: 280px;
    top: 518px;
    font-size: 30px;
  }
  .label-cable {
    left: 480px;
    width: 325px;
    top: 428px;
    font-size: 30px;
  }
  .label-ap {
    left: 830px;
    width: 340px;
    top: 516px;
    font-size: 32px;
  }
  .label-ap .model {
    display: block;
    font-size: 21px;
    margin-top: 4px;
  }
  .troubleshooting {
    position: absolute;
    left: 33px;
    top: 630px;
    width: 1131px;
    height: 231px;
    box-sizing: border-box;
    background: var(--black);
    border: 2.5px solid var(--white);
    padding: 8px 22px 0 22px;
  }
  .troubleshooting h2 {
    margin: 0 0 10px 0;
    font-size: 30px;
    font-weight: 500;
    line-height: 1.2;
  }
  .steps, .substeps {
    list-style: none;
    margin: 0;
    padding: 0;
    font-size: 18.5px;
    line-height: 22px;
    font-weight: 400;
  }
  .steps > li {
    position: relative;
    padding-left: 10px;
  }
  .steps > li::before {
    content: "·";
    position: absolute;
    left: 0;
    font-weight: 600;
  }
  .substeps {
    margin-left: 44px;
  }
  .substeps li {
    position: relative;
    padding-left: 20px;
  }
  .substeps li::before {
    content: "→";
    position: absolute;
    left: 0;
    font-size: 15px;
  }
</style>
</head>
<body>
<main class="splash">
  <div class="brand">
    <div class="brand-name">CGSI</div>
    <div class="brand-full">Copperlane Growing Systems Inc.</div>
  </div>

  <h1 class="headline">Waiting for<br>connection to Wi-Fi<br>access point...</h1>

  <svg class="diagram" viewBox="0 0 1200 620" xmlns="http://www.w3.org/2000/svg">
    <defs>
      <linearGradient id="deviceGradient" x1="0" y1="0" x2="0" y2="1">
        <stop offset="0" stop-color="var(--device-mid)"/>
        <stop offset="1" stop-color="var(--device-dark)"/>
      </linearGradient>
      <linearGradient id="apGradient" x1="0" y1="0" x2="1" y2="0">
        <stop offset="0" stop-color="var(--ap-shade)"/>
        <stop offset="0.5" stop-color="var(--ap-light)"/>
        <stop offset="1" stop-color="var(--ap-shade)"/>
      </linearGradient>
    </defs>
    <path class="ethernet-cable" d="M322 477 H1111 V458" fill="none" stroke="var(--black)" stroke-width="4.5" stroke-linejoin="round"/>
    <rect class="cab-computer" role="img" aria-label="Industrial tractor cab computer showing the seeding application screen" x="24" y="279" width="299" height="237" rx="14" fill="url(#deviceGradient)"/>
    <rect class="wifi-access-point" role="img" aria-label="Outdoor Wi-Fi access point with two antennas" x="1094" y="258" width="37" height="205" rx="8" fill="url(#apGradient)"/>
  </svg>

  <div class="label label-computer">Tractor cab<br>computer</div>
  <div class="label label-cable">Ethernet cable</div>
  <div class="label label-ap">Wi-Fi Access Point<span class="model">Northmesh OAP-220 Outdoor</span></div>

  <section class="troubleshooting">
    <h2>Troubleshooting steps:</h2>
    <ul class="steps">
      <li>This screen should only be visible for a short time on boot.</li>
      <li>If this screen stays visible for more than a minute:
        <ul class="substeps">
          <li>Verify that the Wi-Fi Access Point (AP) powers up when this system does (indicated by a green light on the side of the AP).</li>
          <li>Check the Ethernet cable between this system and the AP for damage, and replace it if necessary.</li>
          <li>Power-cycle this system and wait for it to reboot fully.</li>
          <li>If the issue persists, contact CGSI support for further assistance.</li>
        </ul>
      </li>
    </ul>
  </section>
</main>
</body>
</html>
```